Corlen-Ashby Custom Jewelry Homepage

High-end custom jewelry designer ($10,000-$1 mil.) website design. PSD only for WordPress framework.

Corlen Ashby has a temporary site at http://corlen-ashby-example.com/ and is looking for a permanent design.

We need an elegant WordPress homepage designed that highlights our client's products and presents them as high-end, exclusive pieces of jewelry that are custom designed for each client.

Please see that attached design brief for more information.
Updates

Project Deadline Extended
Reason: Hi Guys, We need a little more time to meet with our client and choose a final design. Thanks,

Project Deadline Extended

Target Market(s)

High end jewelry buyers

Industry/Entity Type

Jewelry

Number of Pages Required

1 page

Requirements
Must have
• Homepage design similar to attached mockups with elegant product banner at top featuring the Corlen Ashby logo in the 4 corners

```html
<!DOCTYPE html>
<html lang="en">
<head>
<meta charset="utf-8">
<title>Corlen-Ashby Custom Jewelry</title>
<link rel="stylesheet" href="https://fonts.googleapis.com/css2?family=Great+Vibes&family=Montserrat:wght@400;500&display=swap">
<style>
  :root {
    --black: #000000;
    --ink: #0b0b0b;
    --tile: #030303;
    --gold-light: #efe2b8;
    --gold: #c9ac6a;
    --gold-deep: #8d6c2e;
    --white: #ffffff;
    --paper: #f4f4f6;
    --text: #1c1c1c;
    --muted: #9a9a9a;
  }
  * { box-sizing: border-box; margin: 0; padding: 0; }
  html, body { width: 1200px; height: 2647px; overflow: hidden; background: var(--black); }
  body { position: relative; font-family: "Montserrat", sans-serif; color: var(--white); }
  .script { font-family: "Great Vibes", cursive; font-weight: 400; }

  /* Hero */
  .hero { position: absolute; left: 0; top: 0; width: 1200px; height: 1382px;
    background: radial-gradient(ellipse at 50% 30%, #1e1e1e 0%, #0c0c0c 45%, #000 100%); }
  .header-band { position: absolute; left: 0; top: 0; width: 1200px; height: 130px; }
  .brand-name { position: absolute; top: 38px; font-size: 26px; font-weight: 500; letter-spacing: 3px;
    text-transform: uppercase; color: #2a1f0c; }
  .brand-name.left { left: 270px; }
  .brand-name.right { left: 690px; }
  .brand-dot { position: absolute; left: 550px; top: 12px; width: 100px; height: 100px; border-radius: 50%;
    border: 3px solid #2a1f0c; }
  .menu-icon { position: absolute; left: 1014px; top: 40px; width: 18px; }
  .menu-icon span { display: block; height: 3px; background: var(--white); margin-bottom: 3px; }
  .corner { position: absolute; width: 86px; height: 96px;
    background: radial-gradient(circle, var(--gold) 0%, var(--gold-deep) 55%, rgba(0,0,0,0) 75%); opacity: .55; }
  .hero-ring { position: absolute; left: 370px; top: 232px; width: 415px; height: 330px; border-radius: 48%;
    background: radial-gradient(ellipse at 50% 45%, #f2f2f2 0%, #b8b8bc 30%, #55565a 60%, rgba(0,0,0,0) 75%); }
  .thumb-strip { position: absolute; left: 106px; top: 620px; width: 988px; height: 176px; background: rgba(0,0,0,.55); }
  .thumb-arrow { position: absolute; top: 688px; width: 14px; height: 22px; }
  .thumb { position: absolute; top: 657px; width: 108px; height: 88px; background: #0a0a0a; border: 1px solid #2b2b2b;
    display: flex; align-items: center; justify-content: center; }
  .thumb.active { top: 620px; left: 523px; width: 152px; height: 125px; border-color: #3a3a3a; }
  .thumb i { display: block; width: 62%; height: 62%; border-radius: 50%;
    background: radial-gradient(circle, #e6e6e8 0%, #8a8b90 45%, rgba(0,0,0,0) 72%); }

  .occasions { position: absolute; left: 201px; top: 870px; width: 798px; display: grid;
    grid-template-columns: 388px 388px; column-gap: 22px; row-gap: 33px; }
  .occasion { height: 205px; background: var(--tile); display: flex; align-items: center; }
  .occasion-photo { width: 190px; height: 150px; margin-left: 8px; border-radius: 40%;
    background: radial-gradient(ellipse, #d9d9dc 0%, #7b7c80 40%, rgba(0,0,0,0) 72%); }
  .occasion-title { font-size: 50px; line-height: 46px; color: var(--white); margin-left: 4px; }

  /* Bride */
  .bride { position: absolute; left: 0; top: 1382px; width: 1200px; height: 512px;
    background: linear-gradient(100deg, #f7f7f9 0%, #e7e7ea 45%, #d8d8dc 100%); }
  .bride-photo { position: absolute; left: 560px; top: 0; width: 500px; height: 512px;
    background: radial-gradient(ellipse at 55% 40%, #e8c9b8 0%, #c7a598 30%, #eaeaea 70%, rgba(232,232,235,0) 100%); }
  .bride-arrow { position: absolute; top: 266px; width: 32px; height: 32px; background: #bdbdbd;
    display: flex; align-items: center; justify-content: center; }
  .bride-copy { position: absolute; left: 191px; top: 200px; color: var(--text); }
  .bride-copy h2 { font-size: 58px; line-height: 64px; color: #111; }
  .bride-copy p { font-size: 14px; margin-top: 2px; }
  .btn { display: inline-block; margin-top: 35px; margin-left: -2px; width: 141px; height: 44px; line-height: 44px;
    text-align: center; background: var(--black); color: var(--white); font-size: 11px; letter-spacing: .5px; }

  /* Testimonials */
  .testimonials { position: absolute; left: 0; top: 1894px; width: 1200px; height: 468px; background: var(--white);
    text-align: center; color: var(--text); }
  .testimonials h2 { margin-top: 100px; font-size: 60px; line-height: 70px; color: #111; }
  .partner { margin-top: 38px; display: inline-flex; flex-direction: column; align-items: center; }
  .partner-mark { width: 20px; height: 20px; border: 2px solid #222; transform: rotate(45deg); }
  .partner-name { margin-top: 12px; font-size: 17px; letter-spacing: 2.5px; text-transform: uppercase; color: #111; }
  .partner-city { font-size: 8px; letter-spacing: 2px; text-transform: uppercase; margin-top: 4px; }
  .quote { width: 830px; margin: 28px auto 0; font-size: 13.5px; line-height: 23px; color: #222; }

  /* Footer */
  .footer { position: absolute; left: 0; top: 2362px; width: 1200px; height: 285px;
    background: radial-gradient(ellipse at 50% 30%, #1a1a1a 0%, #060606 70%); text-align: center; }
  .footer-dot { width: 96px; height: 96px; border-radius: 50%; border: 4px solid var(--white); margin: 22px auto 0; }
  .footer-name { margin-top: 20px; font-size: 22px; font-weight: 500; letter-spacing: 3px; text-transform: uppercase; }
  .footer-address { margin-top: 30px; font-size: 10px; color: #cfcfcf; letter-spacing: .3px; }
  .footer-copy { margin-top: 14px; font-size: 10px; color: #cfcfcf; }
</style>
</head>
<body>

<section class="hero" role="img" aria-label="Dark quilted leather backdrop behind the featured ring">
  <svg class="header-band" viewBox="0 0 1200 130" aria-hidden="true">
    <defs>
      <linearGradient id="goldBand" x1="0" y1="0" x2="1" y2="0">
        <stop offset="0" stop-color="#8d6c2e"/>
        <stop offset=".3" stop-color="#e9d9a6"/>
        <stop offset=".5" stop-color="#f5ecc9"/>
        <stop offset=".7" stop-color="#e9d9a6"/>
        <stop offset="1" stop-color="#8d6c2e"/>
      </linearGradient>
    </defs>
    <path d="M0 0 H1200 V34 Q600 190 0 34 Z" fill="url(#goldBand)"/>
    <path d="M0 34 Q600 190 1200 34" fill="none" stroke="#6e5322" stroke-width="2"/>
  </svg>
  <div class="brand-name left">Corlen Ashby</div>
  <div class="brand-dot"></div>
  <div class="brand-name right">Corlen Ashby</div>
  <div class="menu-icon"><span></span><span></span><span></span></div>

  <div class="corner" style="left:0;top:40px" role="img" aria-label="Gold corner ornament"></div>
  <div class="corner" style="right:0;top:40px" role="img" aria-label="Gold corner ornament"></div>
  <div class="corner" style="left:0;top:680px" role="img" aria-label="Gold corner ornament"></div>
  <div class="corner" style="right:0;top:680px" role="img" aria-label="Gold corner ornament"></div>

  <div class="hero-ring" role="img" aria-label="Oval diamond ring with trillion side stones"></div>

  <div class="thumb-strip"></div>
  <svg class="thumb-arrow" style="left:118px" viewBox="0 0 14 22" aria-hidden="true"><path d="M10 6 L5 11 L10 16" stroke="#fff" stroke-width="2" fill="none"/></svg>
  <div class="thumb" style="left:150px" role="img" aria-label="Ring thumbnail"><i></i></div>
  <div class="thumb" style="left:274px" role="img" aria-label="Ring thumbnail"><i></i></div>
  <div class="thumb" style="left:397px" role="img" aria-label="Ring thumbnail"><i></i></div>
  <div class="thumb active" role="img" aria-label="Selected ring thumbnail"><i></i></div>
  <div class="thumb" style="left:692px" role="img" aria-label="Ring thumbnail"><i></i></div>
  <div class="thumb" style="left:815px" role="img" aria-label="Ring thumbnail"><i></i></div>
  <div class="thumb" style="left:939px" role="img" aria-label="Ring thumbnail"><i></i></div>
  <svg class="thumb-arrow" style="left:1070px" viewBox="0 0 14 22" aria-hidden="true"><path d="M4 6 L9 11 L4 16" stroke="#fff" stroke-width="2" fill="none"/></svg>

  <div class="occasions">
    <div class="occasion"><div class="occasion-photo" role="img" aria-label="Yellow diamond engagement ring"></div><div class="occasion-title script">Engagement<br>Rings</div></div>
    <div class="occasion"><div class="occasion-photo" role="img" aria-label="Emerald cut anniversary ring"></div><div class="occasion-title script">Anniversaries</div></div>
    <div class="occasion"><div class="occasion-photo" role="img" aria-label="Pear diamond birthday ring"></div><div class="occasion-title script">Birthdays</div></div>
    <div class="occasion"><div class="occasion-photo" role="img" aria-label="Halo diamond special occasion ring"></div><div class="occasion-title script">Special<br>Occasion</div></div>
  </div>
</section>

<section class="bride">
  <div class="bride-photo" role="img" aria-label="Bride in a lace gown resting her hand near her neck"></div>
  <div class="bride-arrow" style="left:160px"><svg width="10" height="14" viewBox="0 0 10 14"><path d="M7 2 L3 7 L7 12" stroke="#fff" stroke-width="2" fill="none"/></svg></div>
  <div class="bride-arrow" style="left:1000px"><svg width="10" height="14" viewBox="0 0 10 14"><path d="M3 2 L7 7 L3 12" stroke="#fff" stroke-width="2" fill="none"/></svg></div>
  <div class="bride-copy">
    <h2 class="script">Ever a Bride</h2>
    <p>Ever a Bride is in the process of being Trade Marked</p>
    <a class="btn">REGISTER NOW</a>
  </div>
</section>

<section class="testimonials">
  <h2 class="script">Testimonials</h2>
  <div class="partner">
    <div class="partner-mark"></div>
    <div class="partner-name">The Gem Parlour</div>
    <div class="partner-city">Vienna</div>
  </div>
  <p class="quote">At vero eos et accusamus et iusto odio dignissimos ducimus qui blanditiis praesentium voluptatum deleniti atque corrupti quos dolores et quas molestias excepturi sint occaecati cupiditate non provident, similique sunt in culpa qui officia deserunt mollitia animi, id est laborum et dolorum fuga. Et harum quidem rerum</p>
</section>

<footer class="footer">
  <div class="footer-dot"></div>
  <div class="footer-name">Corlen Ashby</div>
  <div class="footer-address">Harlow Trade Plaza &nbsp;|&nbsp; 410 Linden Ave., Suite 220 &nbsp;|&nbsp; Marston, TX 75000</div>
  <div class="footer-copy">© 2016 Company Name &nbsp;|&nbsp; All Rights Reserved</div>
  <div class="corner" style="left:0;top:190px" role="img" aria-label="Gold corner ornament"></div>
  <div class="corner" style="right:0;top:190px" role="img" aria-label="Gold corner ornament"></div>
</footer>

</body>
</html>
```